Business Card Design Project

This is the first time we use our new logo. We need a business card that we can use both on our institutional corporate relationships and also that works for our staff that deals with consumers directly.

VELUNDA is a new company dedicated to empower consumers and to provide them with the best choices for specialized health care using the latest telemedicine technology (medicine at a distance via videoconference).

We want to print this cards in high quality materials and process. We will like designs that allow us to use UV spot varnish and other techniques that will differentiate us.

We are including Two different versions of Color logos. In addition we are including white over black background logos. Those can be used replacing the black for a color.

Please note this is the first time we will be creating any corporate materials with our new logo and colors.

Target Market(s)

34+ consumers of medium high and high socioeconomic levels.

Industry/Entity Type

Health

Requirements
Must have
• Our logo on its original colors
Should not have
• Any other graphical element or design that is not our logo

```html
<!DOCTYPE html>
<html lang="en">
<head>
<meta charset="utf-8">
<title>VELUNDA Business Card</title>
<link rel="stylesheet" href="https://fonts.googleapis.com/css2?family=Jost:wght@400;600&display=swap">
<style>
  :root {
    --paper: #ffffff;
    --band: #333333;
    --sky: #5bb8e0;
    --teal: #1aa59a;
    --navy: #1b5a84;
  }
  html, body {
    margin: 0;
    padding: 0;
    width: 1200px;
    height: 741px;
    overflow: hidden;
    background: var(--paper);
  }
  .card {
    position: relative;
    width: 1200px;
    height: 741px;
    background: var(--paper);
    overflow: hidden;
  }
  .footer-band {
    position: absolute;
    left: 0;
    top: 662px;
    width: 1200px;
    height: 79px;
    background: var(--band);
  }
  .rule {
    position: absolute;
  }
  .rule--h {
    left: 0;
    width: 1200px;
    height: 4px;
  }
  .rule--v {
    top: 0;
    width: 4px;
    height: 741px;
  }
  .rule--sky { background: var(--sky); }
  .rule--teal { background: var(--teal); }
  .rule--h1 { top: 636px; }
  .rule--h2 { top: 645px; }
  .rule--h3 { top: 654px; }
  .rule--v1 { left: 67px; }
  .rule--v2 { left: 76px; }
  .rule--v3 { left: 85px; }

  .brand {
    position: absolute;
    left: 300px;
    top: 220px;
    display: flex;
    align-items: center;
    gap: 70px;
  }
  .brand__dot {
    width: 110px;
    height: 110px;
    flex: none;
  }
  .brand__name {
    font-family: "Jost", sans-serif;
    font-weight: 600;
    font-size: 98px;
    letter-spacing: 6px;
    color: var(--navy);
    line-height: 1;
    margin-top: 120px;
  }
  .website {
    position: absolute;
    right: 18px;
    top: 668px;
    font-family: "Jost", sans-serif;
    font-weight: 400;
    font-size: 25px;
    letter-spacing: 0.5px;
    color: var(--sky);
  }
</style>
</head>
<body>
  <div class="card">
    <div class="footer-band"></div>

    <div class="rule rule--h rule--sky rule--h1"></div>
    <div class="rule rule--h rule--teal rule--h2"></div>
    <div class="rule rule--h rule--sky rule--h3"></div>

    <div class="rule rule--v rule--sky rule--v1"></div>
    <div class="rule rule--v rule--teal rule--v2"></div>
    <div class="rule rule--v rule--sky rule--v3"></div>

    <div class="brand">
      <svg class="brand__dot" viewBox="0 0 110 110" aria-hidden="true">
        <circle cx="55" cy="55" r="46" fill="none" stroke="var(--sky)" stroke-width="11"/>
      </svg>
      <div class="brand__name">VELUNDA</div>
    </div>

    <div class="website">www.velunda.com</div>
  </div>
</body>
</html>
```